Flyer Design Project

We need a flyer for a company based in Melbourne, Australia.
We offer subscription based E-Commerce/CMS website starting from $20/month. We also do custom web design, custom software development and SEO as additional services.

TREVOLCommerce is our first product, where people can get their site up and running in just seconds.

We would like to designs that sticks to our company branding. Our main color is white/grey/green.
Our complementary color is dark grey and orange.

The final design should deliver the following elements:
- modern
- clean
- easy / playful / fun
- grow (in sales, business)
- friendly

Our goal is to deliver this message to small businesses:
Online shop / website that is
- affordable
- easy to use
- accessible from many devices

Overall look please visit www.trevol-example.com.au

Target Market(s)

small business start ups

Industry/Entity Type

Software

Requirements
Must have
• Must look commercial / selling.
$20/month must be highlighted.
mascot, leaves
stick with the company branding.
Flowing design.

Please allocate a white box in (64mm x 24.3mm) for labelling.
Will be printed in A5, double sided.
Nice to have
• We are using DIN for TREVOL
and MyriadPro for "Your Store Set Up Swiftly", be good if we can stick to the font.
May use the shop image in the attachment, not necessary.
Should not have
• Must not look old / corporate.

```html
<!DOCTYPE html>
<html lang="en">
<head>
<meta charset="utf-8">
<title>TREVOLCommerce Flyer</title>
<link rel="stylesheet" href="https://fonts.googleapis.com/css2?family=Arimo:ital,wght@0,400;0,700;1,400;1,700&family=Barlow:wght@400&family=Open+Sans:wght@400&display=swap">
<style>
  :root {
    --orange: #f26b1d;
    --orange-deep: #e2570e;
    --green: #8cc63f;
    --green-dark: #4f8a1d;
    --ink: #1a1a1a;
    --grey: #4d4d4f;
    --shadow: #cfcfcf;
    --paper: #ffffff;
  }
  * { margin: 0; padding: 0; box-sizing: border-box; }
  html, body { width: 846px; height: 1200px; overflow: hidden; background: var(--paper); }
  .flyer {
    position: relative;
    width: 846px;
    height: 1200px;
    overflow: hidden;
    background: var(--paper);
    font-family: "Arimo", Arial, sans-serif;
    color: var(--ink);
  }
  .backdrop { position: absolute; inset: 0; }
  .brand {
    position: absolute;
    left: 160px;
    top: 58px;
    width: 430px;
    text-align: center;
  }
  .brand__name {
    font-family: "Barlow", "DIN Alternate", sans-serif;
    font-weight: 400;
    font-size: 118px;
    line-height: 1;
    letter-spacing: 2px;
    color: var(--grey);
  }
  .brand__tagline {
    margin-top: 12px;
    font-family: "Open Sans", "Myriad Pro", sans-serif;
    font-size: 36px;
    color: var(--grey);
    letter-spacing: -0.5px;
  }
  .mascot {
    position: absolute;
    left: 606px;
    top: 12px;
    width: 150px;
    height: 190px;
    border-radius: 26px;
    background: linear-gradient(160deg, #a6d65a, var(--green) 60%, #6fa82c);
  }
  .intro {
    position: absolute;
    top: 318px;
    left: 0;
    width: 846px;
    text-align: center;
    font-size: 23px;
    line-height: 36px;
  }
  .pitch {
    position: absolute;
    left: 110px;
    top: 410px;
    font-size: 22px;
    line-height: 33px;
  }
  .pitch__list { list-style: none; }
  .pitch__list li { font-weight: 700; font-style: italic; }
  .pitch__list li::before { content: "- "; font-weight: 400; font-style: normal; }
  .contact {
    position: absolute;
    left: 24px;
    top: 568px;
  }
  .contact__phone {
    font-size: 52px;
    font-weight: 700;
    font-style: italic;
    letter-spacing: -0.5px;
    line-height: 1;
  }
  .contact__address {
    margin-top: 12px;
    font-size: 22px;
    line-height: 35px;
    font-style: normal;
  }
  .branch {
    position: absolute;
    left: 490px;
    top: 390px;
    width: 290px;
    height: 500px;
    border-radius: 50% 50% 45% 55% / 40% 45% 55% 60%;
    background: radial-gradient(ellipse at 50% 42%, #a9d64e 0%, #7cb82f 50%, rgba(124,184,47,0) 72%);
  }
  .price {
    position: absolute;
    left: 390px;
    top: 948px;
    font-style: italic;
  }
  .price__from { font-size: 22px; font-style: normal; }
  .price__amount { font-size: 54px; font-weight: 700; letter-spacing: -1px; }
  .services {
    position: absolute;
    left: 121px;
    top: 1072px;
    font-size: 21px;
    line-height: 32px;
  }
</style>
</head>
<body>
<main class="flyer">
  <svg class="backdrop" width="846" height="1200" viewBox="0 0 846 1200" aria-hidden="true">
    <path d="M0 0 H846 V262 H0 Z" fill="var(--orange)"/>
    <path d="M0 0 H330 C230 30 110 70 0 110 Z" fill="var(--paper)"/>
    <path d="M0 112 C110 70 230 30 330 0 H300 C200 28 100 60 0 92 Z" fill="var(--green)"/>
    <path d="M0 880 C190 760 430 640 846 400 L846 560 C560 640 300 720 0 900 Z" fill="var(--orange)"/>
    <path d="M40 872 C260 760 520 660 846 600 L846 700 C560 690 300 760 40 872 Z" fill="var(--shadow)" opacity="0.6"/>
    <path d="M20 882 C250 770 510 670 846 612 L846 690 C560 680 300 750 20 882 Z" fill="var(--paper)"/>
  </svg>

  <header class="brand">
    <h1 class="brand__name">TREVOL</h1>
    <p class="brand__tagline">Your Store Set Up Swiftly</p>
  </header>
  <div class="mascot" role="img" aria-label="Green box-shaped mascot character"></div>

  <p class="intro">TREVOLCommerce is our first product,<br>where people can get their site up and running in just seconds.</p>

  <section class="pitch">
    <p>Online shop / website that is</p>
    <ul class="pitch__list">
      <li>affordable</li>
      <li>easy to use</li>
      <li>accessible from many devices</li>
    </ul>
  </section>

  <div class="branch" role="img" aria-label="Growing branch with fresh green leaves"></div>

  <section class="contact">
    <p class="contact__phone">1300 555 014</p>
    <address class="contact__address">4/72 Example Street<br>Northfield,&nbsp; VIC - 3099<br>Melbourne</address>
  </section>

  <p class="price"><span class="price__from">from </span><span class="price__amount">$20/month.</span></p>

  <p class="services">We offer subscription based E-Commerce/CMS website starting<br>We also do custom web design,<br>custom software development and SEO as additional services.</p>
</main>
</body>
</html>
```